Brierley Dunmore Lawyers needs a web design

We need a web design for our conveyancing and commercial law firm based in Sydney Australia. We want to depersonalise the current website: http://www.brierleydunmore.example/ and give it a classic modern feel to it. It should be a simple design (possibly one page) and communicate trust, professionalism and experience.

Content should include:

Brierley Dunmore is a boutique Sydney based legal practice specialising in business and property law.

We pride ourselves on our proactive, receptive and dynamic approach to client service. Our business survives on referrals from satisfied clients and professionals who respect the way we do business.

Practice areas

Business law

We act on the sale and purchase of businesses. We assist clients with structuring their businesses, drafting shareholder agreements and buy-sell arrangements. We have acted on a multitude of other commercial matters including franchising, distribution, marketing and business services (with a particular focus in the advertising sector).

Property law

We act for developers, commercial property investors, landlords and tenants. We also handle residential conveyancing and deal with strata and company title matters.

Private Client

We draft wills and codicils on behalf of clients and can also assist with applications for probate should the need arise.

Contact Us

Brierley Dunmore
Level 29, Wexcombe Tower
7 Marlowe Square
Sydney, NSW 2000

t: +61 (0)2 9471 6203
f: +61 (0)2 8526 4079
e: enquiries@brierleydunmore.example

Target Market(s)

Individuals and business who need legal advice in the area of property and commercial law

Industry/Entity Type

Legal

Number of Pages Required

1 page

Font styles to use
Sans Serif

Requirements
Must have
• Clear and concise content.
Nice to have
• Some images to break up the content.
Should not have
• Any offensive images tones or connotations.

```html
<!DOCTYPE html>
<html lang="en">
<head>
<meta charset="utf-8">
<title>Brierley Dunmore Lawyers</title>
<link href="https://fonts.googleapis.com/css2?family=Roboto+Condensed:wght@300;400&family=Roboto:wght@400;500&display=swap" rel="stylesheet">
<style>
:root{
  --navy:#0b2a6b;
  --navy-band:rgba(22,58,120,.82);
  --blue:#1d4f9c;
  --ink:#333a44;
  --muted:#555;
  --grey-btn:#7b7b7b;
  --panel:#f2f2f2;
  --white:#fff;
}
*{margin:0;padding:0;box-sizing:border-box}
html,body{width:747px;height:1200px;overflow:hidden;background:var(--white)}
body{position:relative;font-family:Roboto,Arial,sans-serif;color:var(--ink)}
.abs{position:absolute}
.cond{font-family:"Roboto Condensed","Arial Narrow",sans-serif}

/* header */
.header{left:0;top:0;width:747px;height:68px;background:var(--white)}
.brand{left:46px;top:18px;color:var(--navy);font-family:"Roboto Condensed",sans-serif;font-weight:300;line-height:1}
.brand .name{font-size:23px;display:block}
.brand .sub{font-size:11px;display:block;text-align:right;margin-top:2px}
.top-phone{right:46px;top:14px;font-size:10.5px;color:var(--navy);display:flex;align-items:center;gap:8px}
.nav{right:46px;top:45px;display:flex;gap:26px;font-size:10.5px;color:var(--ink)}
.nav .active{color:var(--navy)}

/* hero */
.hero{left:0;top:68px;width:747px;height:303px;background:linear-gradient(180deg,#8fb8e0 0%,#c9dcec 30%,#7f8d98 55%,#2f6a93 75%,#5d6c70 100%)}
.hero-band{left:0;top:166px;width:747px;height:108px;background:var(--navy-band)}
.hero-title{left:0;top:174px;width:747px;text-align:center;color:var(--white);font-size:29px;line-height:34px;font-weight:400}
.dots{left:352px;top:255px;display:flex;gap:5px}
.dots span{width:6px;height:6px;border-radius:50%;background:#111}
.dots span:first-child{background:var(--white)}

/* welcome */
.welcome-title{left:0;top:398px;width:747px;text-align:center;font-size:21px;font-weight:300;color:#222}
.welcome-title em{font-style:normal;color:var(--blue)}
.welcome-copy{left:40px;top:435px;width:667px;text-align:center;font-size:8.3px;line-height:16px;color:var(--muted)}

/* practice */
.practice{left:0;top:503px;width:747px;height:282px;background:var(--panel)}
.practice-photo{left:0;top:503px;width:206px;height:282px;background:linear-gradient(160deg,#e8ecef 0%,#cfd6dc 45%,#2e3640 100%)}
.practice-title{left:227px;top:521px;font-size:21px;font-weight:300;color:#222}
.practice-title em{font-style:normal;color:var(--blue)}
.card-img{width:224px;height:88px;top:561px}
.card-label{width:224px;height:28px;top:649px;background:var(--navy);color:var(--white);font-size:14px;padding:6px 11px 0}
.card-text{width:224px;top:685px;font-size:8.5px;line-height:15px;color:var(--muted)}
.btn{height:24px;width:78px;background:var(--grey-btn);color:var(--white);font-size:8.8px;font-weight:500;display:flex;align-items:center;justify-content:center;border-bottom:2px solid #5e5e5e}

/* private client */
.private{left:0;top:785px;width:747px;height:135px;background:linear-gradient(90deg,#4b4a46 0%,#6c6a66 40%,#585754 70%,#2e2d2b 100%)}
.private-title{left:0;top:808px;width:747px;text-align:center;color:var(--white);font-size:21px;font-weight:300}
.private-copy{left:0;top:847px;width:747px;text-align:center;color:#eee;font-size:8.5px}

/* map + contact */
.map{left:0;top:920px;width:747px;height:168px;background:linear-gradient(135deg,#ece8df 0%,#e3e0d8 50%,#dfe6d6 100%)}
.footer{left:0;top:1088px;width:747px;height:112px;background:var(--navy)}
.contact-card{left:102px;top:1053px;width:543px;height:67px;background:var(--white);box-shadow:0 1px 3px rgba(0,0,0,.15)}
.card-brand{left:12px;top:18px;color:var(--navy);font-family:"Roboto Condensed",sans-serif;font-weight:300;line-height:1}
.card-brand .name{font-size:19px;display:block}
.card-brand .sub{font-size:9px;display:block;text-align:right;margin-top:2px}
.brace{left:176px;top:10px;font-size:44px;color:#aaa;font-weight:300;font-family:"Roboto Condensed",sans-serif;line-height:1}
.c-item{font-size:8.3px;line-height:13px;color:#333;display:flex;gap:7px;align-items:flex-start}
.footer-nav{left:47px;top:1140px;display:flex;gap:20px;font-size:8.3px;color:var(--white)}
.legal{left:47px;top:1162px;font-size:7.5px;line-height:13px;color:#d8def0}
.social{left:589px;top:1150px;display:flex;gap:5px}
.social span{width:25px;height:25px;border:1.5px solid var(--white);border-radius:50%}
</style>
</head>
<body>

<header class="abs header">
  <div class="abs brand"><span class="name">Brierley Dunmore</span><span class="sub">Lawyers</span></div>
  <div class="abs top-phone">
    <svg width="10" height="10" viewBox="0 0 10 10"><rect width="10" height="10" rx="2" fill="#0b2a6b"/><path d="M3 2.5c.4 2.4 1.8 4 4.2 4.8l.6-1-1.2-.7-.6.6C5 5.6 4.5 5 4.2 4l.6-.6-.7-1.2z" fill="#fff"/></svg>
    +61 (0)2 9471 6203
  </div>
  <nav class="abs nav"><span class="active">Home</span><span>Our People</span><span>Practice Areas</span><span>Testimonials</span><span>Contact Us</span></nav>
</header>

<section class="abs hero" role="img" aria-label="Sydney harbour and city skyline with ferries"></section>
<div class="abs hero-band"></div>
<h1 class="abs hero-title cond">We are a boutique Sydney based legal practice<br>specialising in business and property law.</h1>
<div class="abs dots"><span></span><span></span><span></span><span></span></div>

<h2 class="abs welcome-title cond">Welcome to <em>Brierley Dunmore</em></h2>
<p class="abs welcome-copy">Brierley Dunmore is a boutique Sydney based legal practice specialising in business and property law.<br>We pride ourselves on our proactive, receptive and dynamic approach to client service. Our business survives on referrals from satisfied clients and professionals<br>who respect the way we do business.</p>

<section class="abs practice"></section>
<div class="abs practice-photo" role="img" aria-label="Two professionals in business suits"></div>
<h2 class="abs practice-title cond">Practice <em>Areas</em></h2>

<div class="abs card-img" style="left:227px;background:linear-gradient(180deg,#c4ced8,#8a97a3)" role="img" aria-label="Business meeting around a table"></div>
<div class="abs card-label cond" style="left:227px">Business Law</div>
<p class="abs card-text" style="left:227px">We act on the sale and purchase of businesses. We assist clients with structuring their businesses, drafting shareholder agreements..</p>
<div class="abs btn" style="left:227px;top:741px">Read More</div>

<div class="abs card-img" style="left:477px;background:linear-gradient(180deg,#7d7a74,#2f2e2c)" role="img" aria-label="Model house beside scales of justice"></div>
<div class="abs card-label cond" style="left:477px">Property Law</div>
<p class="abs card-text" style="left:478px;width:228px">We act for developers, commercial property investors, landlords and tenants. We also handle residential conveyancing and deal with strata..</p>
<div class="abs btn" style="left:478px;top:741px">Read More</div>

<section class="abs private" role="img" aria-label="Lawyer consulting with a client, darkened"></section>
<h2 class="abs private-title cond">Private Client</h2>
<p class="abs private-copy">We draft wills and codicils on behalf of clients and can also assist with applications for probate should the need arise.</p>
<div class="abs btn" style="left:335px;top:874px">Read More</div>

<div class="abs map" role="img" aria-label="Street map of central Sydney showing the office location"></div>
<footer class="abs footer"></footer>

<div class="abs contact-card">
  <div class="abs card-brand"><span class="name">Brierley Dunmore</span><span class="sub">Lawyers</span></div>
  <div class="abs brace">{</div>
  <div class="abs c-item" style="left:168px;top:14px;padding-left:0">
    <svg width="9" height="12" viewBox="0 0 9 12" style="margin-left:18px"><path d="M4.5 0A4.5 4.5 0 0 0 0 4.5C0 8 4.5 12 4.5 12S9 8 9 4.5A4.5 4.5 0 0 0 4.5 0zm0 6.3a1.8 1.8 0 1 1 0-3.6 1.8 1.8 0 0 1 0 3.6z" fill="#222"/></svg>
    <span>Level 29, Wexcombe Tower<br>7 Marlowe Square Sydney,<br>NSW 2000</span>
  </div>
  <div class="abs c-item" style="left:306px;top:14px">
    <svg width="11" height="11" viewBox="0 0 10 10"><path d="M1.5 1C2 5 5 8 9 8.5l.8-1.8-2-1.1-1 1C5 6 4 5 3.4 3.3l1-1L3.3.3z" fill="#222"/></svg>
    <span>+61 (0)2 9471 6203</span>
  </div>
  <div class="abs c-item" style="left:428px;top:14px">
    <svg width="12" height="12" viewBox="0 0 12 12"><rect x="0" y="3" width="12" height="9" rx="1" fill="#222"/><rect x="3" y="0" width="6" height="4" fill="#222"/><rect x="3" y="5" width="6" height="2" fill="#fff"/></svg>
    <span>+61 (0)2 8526 4079</span>
  </div>
  <div class="abs c-item" style="left:306px;top:40px">
    <svg width="13" height="10" viewBox="0 0 13 10"><rect width="13" height="10" rx="1" fill="#222"/><path d="M1 1.5l5.5 4 5.5-4" stroke="#fff" fill="none" stroke-width="1.2"/></svg>
    <span>enquiries@brierleydunmore.example</span>
  </div>
</div>

<nav class="abs footer-nav"><span>Home</span><span>Our People</span><span>Practice Areas</span><span>Testimonials</span><span>Contact Us</span></nav>
<p class="abs legal">Copyright © 2015. Company Name All Right Reserved<br>Terms Of Services &nbsp;|&nbsp; Desclaimer</p>
<div class="abs social" aria-label="Social links"><span></span><span></span><span></span><span></span></div>

</body>
</html>
```